Road Construction Company needs business cards

We would like a new business card designed for our business.

We're a road construction company based in Qld, Australia.

Can the business card please have the following information on it.

Name: Brent Halloway
Position: General Manager
Phone: 0491 257 314
Email: Brent.halloway@drovik.com.au
Address: 87 Margrove Ave, Tindale, QLD, 4016
Website: www.drovik.com.au

Visually we'd like the card to be professional and simple.

Attached is our logo.

Our website is www.drovik.com.au

Target Market(s)

Men aged 25-60

Contact Information for Business Card

As listed in project description

Font styles to use
Serif

Requirements
Must have
• Large logo on back of card

```html
<!DOCTYPE html>
<html lang="en">
<head>
<meta charset="utf-8">
<title>Drovik Business Card</title>
<link href="https://fonts.googleapis.com/css2?family=Montserrat:wght@800&family=Roboto:wght@400&display=swap" rel="stylesheet">
<style>
  :root {
    --backdrop: #2b2d31;
    --card-white: #ffffff;
    --brand-blue: #0b55a6;
    --accent-blue: #2ea3d9;
    --text-grey: #4a4a4a;
    --soft-grey: #eef0f3;
  }
  * { box-sizing: border-box; margin: 0; padding: 0; }
  html, body {
    width: 1200px;
    height: 952px;
    overflow: hidden;
    background: var(--backdrop);
  }
  .canvas {
    width: 1200px;
    height: 952px;
    display: flex;
    align-items: center;
    justify-content: center;
    gap: 40px;
  }
  .card {
    width: 540px;
    height: 309px;
    position: relative;
    border-radius: 2px;
    box-shadow: 0 10px 30px rgba(0,0,0,0.35);
    overflow: hidden;
  }
  /* Front */
  .card-front {
    background: var(--card-white);
  }
  .card-front .brand-name {
    position: absolute;
    left: 34px;
    top: 32px;
    font-family: "Montserrat", sans-serif;
    font-weight: 800;
    font-size: 40px;
    letter-spacing: 1px;
    color: var(--brand-blue);
    line-height: 1;
  }
  .contact-list {
    position: absolute;
    left: 34px;
    top: 112px;
    list-style: none;
    font-family: "Roboto", sans-serif;
    font-size: 12px;
    color: var(--text-grey);
    line-height: 1.35;
  }
  .contact-list li {
    display: flex;
    align-items: flex-start;
    gap: 8px;
    margin-bottom: 8px;
  }
  .contact-icon {
    width: 16px;
    height: 16px;
    flex: none;
    border-radius: 3px;
    background: var(--accent-blue);
    display: flex;
    align-items: center;
    justify-content: center;
  }
  .contact-icon svg { width: 11px; height: 11px; }
  .holder {
    position: absolute;
    right: 34px;
    top: 150px;
    text-align: left;
  }
  .holder-name {
    font-family: "Montserrat", sans-serif;
    font-weight: 800;
    font-size: 19px;
    color: var(--brand-blue);
    letter-spacing: 0.3px;
  }
  .holder-role {
    font-family: "Roboto", sans-serif;
    font-size: 12.5px;
    color: var(--text-grey);
    margin-top: 4px;
    padding-bottom: 6px;
    border-bottom: 1.5px solid var(--brand-blue);
    display: inline-block;
    padding-right: 30px;
  }
  /* Back */
  .card-back {
    background: var(--brand-blue);
    display: flex;
    align-items: center;
    justify-content: center;
  }
  .card-back .brand-name {
    font-family: "Montserrat", sans-serif;
    font-weight: 800;
    font-size: 64px;
    letter-spacing: 2px;
    color: var(--card-white);
  }
</style>
</head>
<body>
<main class="canvas">
  <section class="card card-front" aria-label="Business card front">
    <div class="brand-name">DROVIK</div>

    <ul class="contact-list">
      <li>
        <span class="contact-icon">
          <svg viewBox="0 0 12 12"><path d="M6 1a3.5 3.5 0 0 0-3.5 3.5C2.5 7 6 11 6 11s3.5-4 3.5-6.5A3.5 3.5 0 0 0 6 1zm0 4.8a1.3 1.3 0 1 1 0-2.6 1.3 1.3 0 0 1 0 2.6z" fill="#fff"/></svg>
        </span>
        <span>87 Margrove Ave, Tindale<br>QLD, 4016</span>
      </li>
      <li>
        <span class="contact-icon">
          <svg viewBox="0 0 12 12"><path d="M3 1.5l1.6 2.3-1 1a6 6 0 0 0 3.6 3.6l1-1 2.3 1.6-.9 1.5C5.4 10.8 1.2 6.6 1.5 2.4z" fill="#fff"/></svg>
        </span>
        <span>0491 257 314</span>
      </li>
      <li>
        <span class="contact-icon">
          <svg viewBox="0 0 12 12"><rect x="1.5" y="3" width="9" height="6" fill="none" stroke="#fff" stroke-width="1.1"/><path d="M1.5 3l4.5 3.5L10.5 3" fill="none" stroke="#fff" stroke-width="1.1"/></svg>
        </span>
        <span>Brent.halloway@drovik.com.au</span>
      </li>
      <li>
        <span class="contact-icon">
          <svg viewBox="0 0 12 12"><circle cx="6" cy="6" r="4.3" fill="none" stroke="#fff" stroke-width="1"/><path d="M1.7 6h8.6M6 1.7c-2 2.5-2 6.1 0 8.6M6 1.7c2 2.5 2 6.1 0 8.6" fill="none" stroke="#fff" stroke-width="0.9"/></svg>
        </span>
        <span>www.drovik.com.au</span>
      </li>
    </ul>

    <div class="holder">
      <div class="holder-name">BRENT HALLOWAY</div>
      <div class="holder-role">General Manager</div>
    </div>
  </section>

  <section class="card card-back" aria-label="Business card back">
    <div class="brand-name">DROVIK</div>
  </section>
</main>
</body>
</html>
```